Webdesign für  IT-Dienstleistungen
Webdesign für IT-Dienstleistungen
Zielgruppe
Wir bieten IT-Dienstleistungen rund um Handy, PC, Laptop und ZEP.
Zielgruppe sind Privatkunden im unterschiedlichen Alter, die Beratung benötigen oder Probleme haben.
Die Leute werden teilweise nicht super IT-affin sein, also muss das Design gut und die usability einfach sein.
Aufgabenstellung
Anbei sind Logo und Visual die bereits erstellt wurden und verwendet werden können.
Inhalte von https://dev.vameko.com/start/ und https://dev.vameko.com/anfrage/ und das anmeldeformular: https://dev.vameko.com/mein-konto/ soll auch auf der Startseite ersichtlich sein
sollten die Startseite ergeben plus Bilder und Texte, wo auch Konversation mit dem Kunden angezeigt werden kann, wenn eingeloggt.
Die Seite sollte sowohl auf dem barrierearm und responsive sein.

```html
<!DOCTYPE html>
<html lang="de">
<head>
<meta charset="utf-8">
<title>Vameko – Hotline bei Technikproblemen</title>
<link href="https://fonts.googleapis.com/css2?family=Mulish:wght@300;400;600;700;800&display=swap" rel="stylesheet">
<style>
  :root {
    --green: #86a212;
    --grey: #6f7477;
    --text: #6b6f72;
    --dark: #55595c;
    --card: #f6f6f6;
    --line: #c9cbcc;
    --white: #ffffff;
  }
  * { box-sizing: border-box; margin: 0; padding: 0; }
  html, body { width: 1200px; height: 4750px; overflow: hidden; }
  body { font-family: "Mulish", sans-serif; background: var(--white); color: var(--text); position: relative; }

  .site-header { position: absolute; left: 0; top: 0; width: 1200px; height: 205px; background: var(--white); box-shadow: 0 2px 6px rgba(0,0,0,.06); }
  .brand { position: absolute; left: 62px; top: 48px; font-size: 96px; font-weight: 800; letter-spacing: 4px; color: var(--grey); line-height: 1; }
  .menu-toggle { position: absolute; left: 1012px; top: 62px; width: 120px; height: 75px; }
  .menu-toggle span { position: absolute; left: 0; width: 120px; height: 10px; background: var(--green); }

  .hero { position: absolute; left: 0; top: 205px; width: 1200px; height: 1232px; }
  .hero-visual { position: absolute; inset: 0; background: linear-gradient(110deg, #eef1ef 0%, #e3e7e6 45%, #d6dadb 70%, #e9ecec 100%); }
  .hero-title { position: absolute; left: 62px; top: 395px; color: var(--green); font-weight: 700; line-height: 1.05; }
  .hero-title .main { display: block; font-size: 88px; }
  .hero-title .sub { display: block; font-size: 60px; margin-top: 8px; }
  .hero-text { position: absolute; left: 62px; top: 655px; width: 1100px; font-size: 42px; line-height: 67px; font-weight: 300; color: var(--text); }
  .hero-sign { position: absolute; left: 62px; top: 995px; font-size: 42px; line-height: 67px; font-weight: 300; }
  .hero-sign strong { font-weight: 700; color: var(--dark); }

  .card { position: absolute; left: 62px; width: 1071px; background: var(--card); border-radius: 6px; box-shadow: 0 2px 6px rgba(0,0,0,.12); overflow: hidden; }
  .card-head { height: 198px; display: flex; align-items: center; padding-left: 92px; color: var(--white); font-size: 60px; font-weight: 600; }
  .card-head svg { width: 112px; height: 112px; margin-right: 50px; }
  .card-request { top: 1510px; height: 1232px; }
  .card-request .card-head { background: var(--green); }
  .card-login { top: 2822px; height: 1233px; }
  .card-login .card-head { background: var(--grey); }

  .field-label { position: absolute; left: 98px; font-size: 38px; font-weight: 700; color: var(--dark); }
  .field { position: absolute; left: 98px; width: 877px; background: var(--white); border: 2px solid #c8c8c8; }
  .btn { position: absolute; left: 98px; width: 877px; height: 107px; background: var(--green); color: var(--white); border-radius: 6px; box-shadow: 0 3px 6px rgba(0,0,0,.2); display: flex; align-items: center; justify-content: center; font-size: 42px; font-weight: 700; }
  .btn svg { margin-left: 45px; }
  .step { position: absolute; left: 0; width: 100%; text-align: center; font-size: 38px; }
  .intro { position: absolute; left: 92px; top: 300px; width: 860px; font-size: 37px; line-height: 60px; font-weight: 400; }
  .forgot { position: absolute; left: 0; width: 100%; text-align: center; font-size: 38px; text-decoration: underline; }

  .contact { position: absolute; left: 0; width: 1200px; display: flex; justify-content: center; align-items: center; font-size: 64px; font-weight: 600; color: var(--grey); }
  .contact svg { margin-right: 35px; }
  .rule { position: absolute; left: 62px; top: 4592px; width: 1071px; height: 3px; background: var(--line); }
  .footer-links { position: absolute; left: 0; top: 4665px; width: 1200px; text-align: center; font-size: 40px; color: var(--text); }
  .footer-links span { margin: 0 18px; }
</style>
</head>
<body>
  <header class="site-header">
    <div class="brand">VAMEKO</div>
    <div class="menu-toggle" aria-label="Menü"><span style="top:0"></span><span style="top:32px"></span><span style="top:65px"></span></div>
  </header>

  <section class="hero">
    <div class="hero-visual" role="img" aria-label="Helles Foto eines Hotline-Mitarbeiters mit Headset am Arbeitsplatz"></div>
    <h1 class="hero-title"><span class="main">Willkommen bei Vameko -</span><span class="sub">ihrer Hotline bei Technikproblemen</span></h1>
    <p class="hero-text">Unser Ziel ist es unabhängigen Technikberatung für alle Interessenten zu bieten und eine schnelle und transpartente Unterstützung bei Problemfällen zu bieten.</p>
    <p class="hero-sign">Im Namen des VaMeKo Teams,<br><strong>Dominik, Clemens und Paul</strong></p>
  </section>

  <section class="card card-request">
    <div class="card-head">
      <svg viewBox="0 0 112 112"><circle cx="56" cy="56" r="56" fill="#fff"/><path d="M56 28v56M28 56h56" stroke="#86a212" stroke-width="6"/></svg>
      NEUE ANFRAGE
    </div>
    <div class="field-label" style="top:290px;font-size:37px">Bitte beschreiben Sie uns Ihr Problem:</div>
    <div class="field" style="top:352px;height:550px"></div>
    <div class="btn" style="top:945px">weiter
      <svg width="72" height="36" viewBox="0 0 72 36"><path d="M2 18h64M50 4l16 14-16 14" fill="none" stroke="#fff" stroke-width="5"/></svg>
    </div>
    <div class="step" style="top:1105px">Schritt 1 von 2</div>
  </section>

  <section class="card card-login">
    <div class="card-head">
      <svg viewBox="0 0 112 112"><circle cx="56" cy="56" r="56" fill="#fff"/><circle cx="56" cy="44" r="16" fill="none" stroke="#6f7477" stroke-width="5"/><path d="M30 86c0-16 12-24 26-24s26 8 26 24" fill="none" stroke="#6f7477" stroke-width="5"/></svg>
      ANMELDUNG
    </div>
    <p class="intro">Geben Sie Ihren Benutzernamen und Ihr Passwort ein, um sich an der Website anzumelden:</p>
    <div class="field-label" style="top:512px">Benutzername:</div>
    <div class="field" style="top:580px;height:112px"></div>
    <div class="field-label" style="top:722px">Passwort:</div>
    <div class="field" style="top:788px;height:112px"></div>
    <div class="btn" style="top:945px">Anmelden</div>
    <div class="forgot" style="top:1102px">Passwort vergessen?</div>
  </section>

  <div class="contact" style="top:4228px">
    <svg width="58" height="92" viewBox="0 0 58 92"><rect x="3" y="3" width="52" height="86" rx="8" fill="none" stroke="#86a212" stroke-width="6"/><rect x="10" y="14" width="38" height="56" fill="#86a212"/><circle cx="29" cy="79" r="4" fill="#86a212"/></svg>
    0041615550199
  </div>
  <div class="contact" style="top:4355px">
    <svg width="80" height="60" viewBox="0 0 80 60"><rect x="0" y="0" width="80" height="60" rx="6" fill="#86a212"/><path d="M4 6l36 28 36-28" fill="none" stroke="#fff" stroke-width="5"/></svg>
    support@vameko.com
  </div>

  <div class="rule"></div>
  <nav class="footer-links"><span>AGB</span>|<span>Datenschutz</span>|<span>Impressum</span></nav>
</body>
</html>
```